8X8 Realtor Training Expo Flyer

BRAVO SUMMIT REALTY & HALCYON REALTY VENTURES
INVITE ALL TO OUR
LIVE REALTOR TRAINING EXPO

WITH TRAINER / SPEAKER MR. GORDON ALAPATI
SATURDAY AUGUST 13th
9 AM - 1 PM
AT THE MARWICK LODGE
4817 HOLLOWAY CREEK DRIVE
GREENBELT, MD 20770

RSVP PREFERRED BY EMAILING FRONTDESK@BRAVOSUMMITREALTY.COM

```html
<!DOCTYPE html>
<html lang="en">
<head>
<meta charset="utf-8">
<title>Live Realtor Training Expo</title>
<link href="https://fonts.googleapis.com/css2?family=Great+Vibes&family=Lobster&family=Montserrat:wght@500;600;700&family=Playfair+Display:wght@700&display=swap" rel="stylesheet">
<style>
  :root {
    --teal: #0a9aa8;
    --teal-light: #14afbd;
    --teal-deep: #0789a0;
    --ink: #1a1a1a;
    --charcoal: #3a3a3a;
    --night: #1c1c1c;
    --white: #ffffff;
  }
  html, body {
    margin: 0;
    padding: 0;
    width: 1200px;
    height: 1200px;
    overflow: hidden;
    background: var(--white);
  }
  .flyer {
    position: relative;
    width: 1200px;
    height: 1200px;
    overflow: hidden;
    font-family: "Montserrat", sans-serif;
    color: var(--ink);
  }
  .flyer-shapes,
  .speaker-photo {
    position: absolute;
    inset: 0;
  }
  .headline {
    position: absolute;
    top: 70px;
    left: 0;
    width: 1200px;
    text-align: center;
    color: var(--white);
  }
  .headline-script {
    font-family: "Great Vibes", cursive;
    font-size: 168px;
    line-height: 1;
    margin: 0;
    font-weight: 400;
  }
  .headline-title {
    font-weight: 600;
    font-size: 57px;
    letter-spacing: 1px;
    margin: 4px 0 0;
  }
  .event-details {
    position: absolute;
    left: 117px;
    top: 420px;
    width: 564px;
    text-align: center;
  }
  .speaker-label {
    font-weight: 500;
    font-size: 31px;
    margin: 0;
  }
  .speaker-name {
    font-family: "Lobster", cursive;
    font-size: 70px;
    color: var(--teal-deep);
    margin: 4px 0 18px;
    line-height: 1.1;
    white-space: nowrap;
  }
  .event-date {
    background: var(--charcoal);
    color: var(--white);
    font-weight: 600;
    font-size: 35px;
    height: 54px;
    line-height: 54px;
    margin: 0;
  }
  .event-time {
    font-weight: 600;
    font-size: 36px;
    margin: 8px 0 0;
  }
  .venue-divider {
    display: flex;
    align-items: center;
    gap: 10px;
    margin: 10px 25px 0;
  }
  .venue-divider .rule {
    flex: 1;
    height: 2px;
    background: var(--teal);
  }
  .venue-name {
    font-family: "Playfair Display", serif;
    font-weight: 700;
    font-size: 33px;
    margin: 4px 25px 0;
    padding-bottom: 10px;
    border-bottom: 2px solid var(--teal);
  }
  .venue-address {
    font-weight: 500;
    font-size: 31px;
    line-height: 40px;
    margin: 18px 0 0;
  }
  .partner-names {
    position: absolute;
    top: 975px;
    left: 115px;
    display: flex;
    gap: 20px;
  }
  .partner-name {
    font-weight: 700;
    font-size: 22px;
    line-height: 28px;
    color: var(--teal-deep);
    text-align: center;
    width: 240px;
    margin: 0;
  }
  .rsvp-bar {
    position: absolute;
    top: 1093px;
    left: 110px;
    width: 980px;
    height: 60px;
    display: flex;
    border-radius: 30px;
    overflow: hidden;
    background: var(--charcoal);
    color: var(--white);
    font-weight: 700;
    font-size: 23px;
    letter-spacing: 0.5px;
  }
  .rsvp-label {
    width: 445px;
    line-height: 60px;
    padding-left: 30px;
    box-sizing: border-box;
    white-space: nowrap;
  }
  .rsvp-email {
    flex: 1;
    background: var(--night);
    border-radius: 30px;
    line-height: 60px;
    text-align: center;
    font-size: 22px;
    white-space: nowrap;
  }
</style>
</head>
<body>
<main class="flyer">
  <svg class="flyer-shapes" width="1200" height="1200" viewBox="0 0 1200 1200" aria-hidden="true">
    <defs>
      <linearGradient id="tealBand" x1="0" y1="0" x2="1" y2="1">
        <stop offset="0" stop-color="#14afbd"/>
        <stop offset="1" stop-color="#0789a0"/>
      </linearGradient>
      <linearGradient id="panelTone" x1="0" y1="0" x2="1" y2="1">
        <stop offset="0" stop-color="#e2e2e2"/>
        <stop offset="0.6" stop-color="#f3f3f3"/>
        <stop offset="1" stop-color="#e6e6e6"/>
      </linearGradient>
    </defs>
    <rect x="0" y="0" width="1200" height="360" fill="url(#tealBand)"/>
    <rect x="0" y="360" width="1200" height="540" fill="url(#panelTone)"/>
    <path d="M665 360 L800 490 Q830 515 870 515 L1200 515 L1200 360 Z" fill="url(#tealBand)"/>
    <path d="M665 360 L695 360 L810 500 L790 500 Z" fill="#2d2d2d"/>
    <rect x="0" y="900" width="1200" height="220" fill="#ffffff"/>
    <rect x="0" y="1120" width="1200" height="80" fill="url(#tealBand)"/>
  </svg>

  <svg class="speaker-photo" width="1200" height="1200" viewBox="0 0 1200 1200" role="img" aria-label="Portrait photo of the trainer in a dark suit and red tie">
    <defs>
      <linearGradient id="photoTone" x1="0" y1="0" x2="0.4" y2="1">
        <stop offset="0" stop-color="#4a3028"/>
        <stop offset="1" stop-color="#1e1613"/>
      </linearGradient>
    </defs>
    <path d="M760 365 L1200 365 L1200 1055 L760 1055 Q730 1055 712 1030 L690 998 Q680 984 680 965 L680 445 Q680 365 760 365 Z" fill="url(#photoTone)"/>
  </svg>

  <header class="headline">
    <h1 class="headline-script">Invite all to Our</h1>
    <p class="headline-title">LIVE REALTOR TRAINING EXPO</p>
  </header>

  <section class="event-details">
    <p class="speaker-label">WITH TRAINER / SPEAKER</p>
    <p class="speaker-name">Mr. Gordon Alapati</p>
    <p class="event-date">SATURDAY, AUGUST 13th</p>
    <p class="event-time">9 AM - 1 PM</p>
    <div class="venue-divider">
      <span class="rule"></span>
      <svg width="20" height="30" viewBox="0 0 20 30" aria-hidden="true">
        <path d="M10 2 C5 2 2 5.5 2 9.5 C2 15 10 22 10 22 C10 22 18 15 18 9.5 C18 5.5 15 2 10 2 Z" fill="none" stroke="#0a9aa8" stroke-width="2.5"/>
        <circle cx="10" cy="9.5" r="3" fill="#0a9aa8"/>
        <ellipse cx="10" cy="26" rx="8" ry="2.5" fill="none" stroke="#0a9aa8" stroke-width="2"/>
      </svg>
      <span class="rule"></span>
    </div>
    <p class="venue-name">AT THE MARWICK LODGE</p>
    <p class="venue-address">4817 HOLLOWAY CREEK DRIVE<br>GREENBELT, MD 20770</p>
  </section>

  <section class="partner-names">
    <p class="partner-name">BRAVO SUMMIT<br>REALTY GROUP</p>
    <p class="partner-name">HALCYON REALTY<br>VENTURES</p>
  </section>

  <footer class="rsvp-bar">
    <span class="rsvp-label">RSVP PREFERRED BY EMAILING</span>
    <span class="rsvp-email">FRONTDESK@BRAVOSUMMITREALTY.COM</span>
  </footer>
</main>
</body>
</html>
```